Hochzeitseinladung im Pocketfold-Style
Zielgruppe
Vertrieb von Hochzeitspapeterie. Unsere Zielgruppe ist weiblich, verlobt, 20 - 40 Jahre alt.
Aufgabenstellung
Wir benötigen ein Design für die Einladungskarte + Einleger in einen Pocketfoldumschlag (Umschlag soll nicht gestaltet werden).
EINLADUNGSTEXT
Formate in mm:130x130mm
Vorgabe für Design / Layout:
Schlichtes Design ohne aufwendige Grafiken mit leichtem Hauch zum Vintage ("Vintage Wedding Icons" z.B. Girlande, Zweig, Retro-Icons wie Vintage Fahrrad, Vogelkäfig, Lampions, etc).
Evtl. oben Initialen C und S unterbringen
Schrift: Farbe dunkelgrau, Font (nur lizenzfreie)
Keine Verwendung von Sonderfarben
Farben Dokument gesamt incl. Grafiken und Objekten: Max. 3 Farben (z.b. Mix aus Grau, Koralle, Altrosa, Mint)
Keine Fotos
EINLEGER
3 x Format in mm: 130x130mm
- Hier nur ein Design für die Überschrift passend zum Einladungsdesign
(3 Überschriften: Unser Tag + Hotel & Anreise + RSVP/Antwort)
Abnahme:
Designbeispiele als pdf zur Korrektur/Abnahme
Fertiges Design soll am Ende als InDesign File sowie als druckfähige pdf-Datei an Käufer gesendet werden.
Vom Gewinner-Design gehen alle Rechte zur kommerziellen Nutzung an den Käufer über.

```html
<!DOCTYPE html>
<html lang="de">
<head>
<meta charset="utf-8">
<title>Hochzeitseinladung Clara &amp; Simon</title>
<link rel="stylesheet" href="https://fonts.googleapis.com/css2?family=Libre+Bodoni:wght@400;700&family=Norican&family=Roboto:wght@300;400&display=swap">
<style>
  :root {
    --rose: #dba89c;
    --rose-light: #f3dcd6;
    --grey: #8c8c8c;
    --grey-light: #cfcfcf;
    --grey-dark: #5e5e5e;
    --paper: #ffffff;
    --backdrop: #d9d9d9;
  }
  * { margin: 0; padding: 0; box-sizing: border-box; }
  html, body { width: 750px; height: 1200px; overflow: hidden; }
  body { background: var(--backdrop); font-family: "Roboto", sans-serif; color: var(--grey-dark); position: relative; }

  .card { position: absolute; background: var(--paper); box-shadow: 0 2px 6px rgba(0,0,0,.12); }
  .invitation { left: 65px; top: 50px; width: 620px; height: 620px; }
  .invitation > * { position: absolute; }

  .couple { top: 52px; left: 0; width: 100%; display: flex; justify-content: center; align-items: center; gap: 16px; }
  .couple__name { font-family: "Libre Bodoni", serif; font-weight: 700; font-size: 19px; letter-spacing: 3px; color: var(--grey); }
  .couple__dot { width: 10px; height: 10px; border-radius: 50%; background: var(--rose); }

  .tagline { top: 118px; width: 100%; text-align: center; font-family: "Norican", cursive; font-size: 27px; color: var(--rose); }
  .occasion { top: 163px; width: 100%; text-align: center; font-weight: 300; font-size: 15px; letter-spacing: 1.4px; line-height: 19px; color: var(--grey); }

  .weekday { left: 64px; top: 386px; transform: rotate(-90deg); transform-origin: left top; font-weight: 300; font-size: 19px; letter-spacing: 1.5px; color: var(--grey); }
  .date { left: 92px; top: 262px; text-align: center; color: var(--rose); font-family: "Libre Bodoni", serif; }
  .date__day { display: block; font-size: 56px; line-height: 56px; }
  .date__month { display: block; font-family: "Roboto", sans-serif; font-weight: 400; font-size: 24px; letter-spacing: 1px; line-height: 28px; }
  .date__year { display: block; font-size: 22px; line-height: 30px; }

  .schedule-frame { left: 188px; top: 240px; }

  .schedule { left: 214px; top: 302px; }
  .schedule__row { display: flex; align-items: center; height: 48px; }
  .schedule__time { font-family: "Libre Bodoni", serif; font-size: 26px; color: var(--rose); width: 78px; }
  .schedule__label { font-size: 11px; letter-spacing: 1.3px; line-height: 12px; color: var(--grey); }

  .venues { left: 418px; top: 302px; }
  .venue { height: 48px; }
  .venue__name { font-family: "Norican", cursive; font-size: 18px; line-height: 22px; color: var(--rose); }
  .venue__place { font-size: 7.5px; letter-spacing: 1px; color: var(--grey); }

  .message { top: 418px; width: 100%; text-align: center; font-family: "Norican", cursive; font-size: 17px; line-height: 25px; color: var(--rose); }

  .rsvp-ribbon { left: 180px; top: 524px; }
  .rsvp-ribbon text { font-family: "Libre Bodoni", serif; font-size: 10px; letter-spacing: 1.2px; fill: #fff; }

  .sender { top: 568px; width: 100%; text-align: center; font-size: 11px; letter-spacing: .8px; line-height: 15px; color: var(--grey-dark); }

  .insert { top: 720px; width: 210px; height: 210px; }
  .insert--day { left: 40px; }
  .insert--travel { left: 270px; }
  .insert--reply { left: 500px; }
  .insert__head { position: absolute; top: 22px; left: 0; width: 100%; display: flex; align-items: center; justify-content: center; gap: 8px; }
  .insert__rule { width: 28px; border-top: 1px dotted var(--grey); }
  .insert__title { font-family: "Norican", cursive; font-size: 20px; color: var(--rose); }
  .insert__sub { position: absolute; top: 52px; width: 100%; text-align: center; font-size: 7px; letter-spacing: 1.3px; color: var(--grey); }
  .insert__footer { position: absolute; bottom: 12px; width: 100%; text-align: center; font-family: "Libre Bodoni", serif; font-weight: 700; font-size: 6px; letter-spacing: 1px; color: var(--grey); }
</style>
</head>
<body>

<section class="card invitation" aria-label="Einladungskarte">
  <header class="couple">
    <span class="couple__name">CLARA</span>
    <span class="couple__dot"></span>
    <span class="couple__name">SIMON</span>
  </header>

  <p class="tagline">Come away with us</p>
  <p class="occasion">TO A WEDDING WEEKEND<br>in THE WOLDS, England</p>

  <p class="weekday">SONNTAG</p>
  <p class="date">
    <span class="date__day">09</span>
    <span class="date__month">JULI</span>
    <span class="date__year">2017</span>
  </p>

  <svg class="schedule-frame" width="216" height="150" viewBox="0 0 216 150">
    <defs>
      <linearGradient id="garland-tone" x1="0" x2="1" y1="0" y2="0">
        <stop offset="0" stop-color="var(--rose-light)"/>
        <stop offset=".5" stop-color="var(--grey-light)"/>
        <stop offset="1" stop-color="var(--rose-light)"/>
      </linearGradient>
    </defs>
    <rect x="8" y="4" width="196" height="40" rx="3" fill="url(#garland-tone)" role="img" aria-label="Illustration: Wimpelgirlande in Altrosa und Grau"/>
    <line x1="2" y1="2" x2="2" y2="148" stroke="var(--grey)" stroke-width="1" stroke-dasharray="1.5 2.5"/>
    <line x1="208" y1="2" x2="204" y2="148" stroke="var(--grey)" stroke-width="1" stroke-dasharray="1.5 2.5"/>
  </svg>

  <div class="schedule">
    <div class="schedule__row"><span class="schedule__time">14.00</span><span class="schedule__label">ZEREMONIE</span></div>
    <div class="schedule__row"><span class="schedule__time">18.30</span><span class="schedule__label">RESTAURANT<br>&amp; HOTEL</span></div>
  </div>

  <div class="venues">
    <div class="venue"><p class="venue__name">The Manor House</p><p class="venue__place">IN LOWER VILLAGE</p></div>
    <div class="venue"><p class="venue__name">The Porch</p><p class="venue__place">IN STOWARD</p></div>
  </div>

  <p class="message">Wir feiern unsere Hochzeit und möchten diesen<br>schönen Moment gerne mit Euch gemeinsam erleben.</p>

  <svg class="rsvp-ribbon" width="240" height="28" viewBox="0 0 240 28">
    <polygon points="0,2 240,2 232,14 240,26 0,26 8,14" fill="var(--rose)"/>
    <text x="120" y="18" text-anchor="middle">ANTWORT BITTE BIS 31. MÄRZ</text>
  </svg>

  <p class="sender">Familie Beispielhaus | Lindenweg 4 | 2345 Beispielstadt<br>family@beispielhaus.de | +49 555 010203</p>
</section>

<section class="card insert insert--day" aria-label="Einleger Unser Tag">
  <div class="insert__head"><span class="insert__rule"></span><span class="insert__title">Unser Tag</span><span class="insert__rule"></span></div>
  <p class="insert__footer">CLARA &amp; SIMON</p>
</section>

<section class="card insert insert--travel" aria-label="Einleger Hotel und Anreise">
  <div class="insert__head"><span class="insert__rule"></span><span class="insert__title">Hotel &amp; Anreise</span><span class="insert__rule"></span></div>
  <p class="insert__footer">CLARA &amp; SIMON</p>
</section>

<section class="card insert insert--reply" aria-label="Einleger RSVP Antwort">
  <div class="insert__head"><span class="insert__rule"></span><span class="insert__title">RSVP</span><span class="insert__rule"></span></div>
  <p class="insert__sub">ANTWORT</p>
  <p class="insert__footer">CLARA &amp; SIMON</p>
</section>

</body>
</html>
```